Trailer Lettering or Partial Wrap

I purchased a new gloss black 7' wide x 12' long x 7' height enclosed cargo trailer that I would like to brand for advertising. on all 4 sides. Our font is AgencyFB (and we only use lower case letters). To reduce cost I thought using the black gloss background could be achieved and use cut out vinyl rather than full wrap unless there are some other ideas. Our colors are Black, White, and Red (HEX #BE1E2D. Items to be displayed:
- logo
- phone # (405) 555-0147
- email. catering@thekelpdockok.com
- web address: www.thekelpdockok.com
- our 2 restaurant locations
- "Edmond" 4870 SE 52nd, Edmond OK 73025
- "NW-OKC" 2915 E Larkspur Rd, Oklahoma City, OK 73159

we would also like to highlight 3 services we offer:
- Catering
- Rent-A-Chef Events
- Sushi Making Classes

For reference our chopsticks from the logo files we use on a lot of print items. Not that I want it to be like this, but I did attach a sample of what ChatGPT created though is in an unusable format and fonts aren't consistent. As well a recent 2' x 4' sign we had made to use on table displays.

We also do like the wording on that last item of " Sushi | Experience | Elevated"

```html
<!DOCTYPE html>
<html lang="en">
<head>
<meta charset="utf-8">
<title>the kelp dock – trailer lettering</title>
<link href="https://fonts.googleapis.com/css2?family=Saira+Extra+Condensed:wght@400;500&display=swap" rel="stylesheet">
<style>
:root{
  --stage:#cccccc;
  --black:#000000;
  --white:#ffffff;
  --bright-red:#e30613;
  --rule:#8a1620;
  --frame:#c8c8c8;
  --frame-dark:#9a9a9a;
}
*{box-sizing:border-box;margin:0;padding:0}
html,body{width:1200px;height:1001px;overflow:hidden;background:var(--stage)}
body{position:relative;font-family:"Saira Extra Condensed","Arial Narrow",sans-serif;color:var(--white);white-space:nowrap}
.panel{position:absolute;background:var(--black);top:265px;height:471px;overflow:hidden}
.side-panel{left:40px;width:230px}
.long-panel{left:297px;width:863px}
.abs{position:absolute}

.brand{position:absolute;display:flex;align-items:center;gap:8px}
.brand-dot{border-radius:50%;background:var(--bright-red);flex:none}
.brand-name{font-weight:500;line-height:.86;color:var(--white)}
.brand-name span{display:block}

.rule{position:absolute;height:1px;background:var(--rule)}
.web-band{position:absolute;background:var(--bright-red);display:flex;align-items:center;justify-content:center;color:var(--black)}

.service-icon{position:absolute}
.service-label{position:absolute;font-size:13px;line-height:1.05;color:var(--white)}
.side-panel .service-label{font-size:10px;width:66px;text-align:center}

.tagline{position:absolute;left:435px;top:87px}
.tagline-line{display:block;border-left:3px solid var(--bright-red);padding-left:10px;font-size:25px;line-height:34px;margin-bottom:6px}

.city{color:var(--bright-red);font-size:13px;line-height:18px}
.address{font-size:13px;line-height:18px}

.door{position:absolute;left:597px;top:73px;width:192px;height:376px;background:var(--frame);border:1px solid var(--frame-dark)}
.door-inner{position:absolute;left:14px;top:14px;right:14px;bottom:14px;background:var(--black)}
</style>
</head>
<body>

<section class="panel side-panel">
  <div class="brand" style="left:48px;top:38px">
    <div class="brand-dot" style="width:12px;height:12px"></div>
    <div class="brand-name" style="font-size:34px"><span>the</span><span>kelp</span><span>dock</span></div>
  </div>

  <svg class="abs" style="left:36px;top:172px" width="16" height="16" viewBox="0 0 16 16" aria-hidden="true">
    <circle cx="8" cy="8" r="7" fill="none" stroke="var(--bright-red)" stroke-width="1.5"/>
    <path d="M5.5 5 l1.5 -.5 1 2 -1 .8 a4 4 0 0 0 2 2 l.8 -1 2 1 -.5 1.5 c-3 .5 -6.5 -3 -5.8 -5.8z" fill="var(--white)"/>
  </svg>
  <div class="abs" style="left:54px;top:166px;font-size:22px;line-height:28px">(405) 555-0147</div>

  <svg class="abs" style="left:36px;top:207px" width="16" height="16" viewBox="0 0 16 16" aria-hidden="true">
    <circle cx="8" cy="8" r="7" fill="none" stroke="var(--bright-red)" stroke-width="1.5"/>
    <rect x="4.5" y="5.5" width="7" height="5" fill="none" stroke="var(--white)" stroke-width=".9"/>
    <path d="M4.5 5.5 8 8.3 11.5 5.5" fill="none" stroke="var(--white)" stroke-width=".9"/>
  </svg>
  <div class="abs" style="left:56px;top:206px;font-size:12px;line-height:18px">catering@thekelpdockok.com</div>

  <div class="web-band" style="left:30px;top:233px;width:170px;height:18px;font-size:12px">www.thekelpdockok.com</div>

  <div class="rule" style="left:20px;top:272px;width:190px"></div>

  <svg class="service-icon" style="left:31px;top:290px" width="38" height="38" viewBox="0 0 38 38" aria-hidden="true">
    <circle cx="19" cy="19" r="17" fill="none" stroke="var(--bright-red)" stroke-width="3"/>
    <path d="M11 22 a8 8 0 0 1 16 0z" fill="none" stroke="var(--white)" stroke-width="1.5"/>
    <line x1="9" y1="24" x2="29" y2="24" stroke="var(--white)" stroke-width="1.5"/>
    <circle cx="19" cy="13" r="1.3" fill="var(--white)"/>
  </svg>
  <div class="service-label" style="left:17px;top:336px">catering</div>

  <svg class="service-icon" style="left:97px;top:290px" width="38" height="38" viewBox="0 0 38 38" aria-hidden="true">
    <circle cx="19" cy="19" r="17" fill="none" stroke="var(--bright-red)" stroke-width="3"/>
    <path d="M14 20 a4 4 0 1 1 3 -7 a4 4 0 0 1 5 0 a4 4 0 1 1 3 7 v5 h-11z" fill="none" stroke="var(--white)" stroke-width="1.5"/>
  </svg>
  <div class="service-label" style="left:83px;top:332px">rent-a-chef<br>events</div>

  <svg class="service-icon" style="left:164px;top:290px" width="38" height="38" viewBox="0 0 38 38" aria-hidden="true">
    <circle cx="19" cy="19" r="17" fill="none" stroke="var(--bright-red)" stroke-width="3"/>
    <ellipse cx="14" cy="18" rx="5" ry="2" fill="none" stroke="var(--white)" stroke-width="1.2"/>
    <path d="M9 18 v5 a5 2 0 0 0 10 0 v-5" fill="none" stroke="var(--white)" stroke-width="1.2"/>
    <ellipse cx="24" cy="15" rx="5" ry="2" fill="none" stroke="var(--white)" stroke-width="1.2"/>
    <path d="M19 15 v5 a5 2 0 0 0 10 0 v-5" fill="none" stroke="var(--white)" stroke-width="1.2"/>
  </svg>
  <div class="service-label" style="left:150px;top:332px">sushi making<br>classes</div>
</section>

<section class="panel long-panel">
  <div class="brand" style="left:60px;top:72px">
    <div class="brand-dot" style="width:18px;height:18px"></div>
    <div class="brand-name" style="font-size:62px"><span>the</span><span>kelp</span><span>dock</span></div>
  </div>

  <svg class="service-icon" style="left:276px;top:58px" width="42" height="42" viewBox="0 0 38 38" aria-hidden="true">
    <circle cx="19" cy="19" r="17" fill="none" stroke="var(--bright-red)" stroke-width="2.5"/>
    <path d="M11 22 a8 8 0 0 1 16 0z" fill="none" stroke="var(--white)" stroke-width="1.3"/>
    <line x1="9" y1="24" x2="29" y2="24" stroke="var(--white)" stroke-width="1.3"/>
    <circle cx="19" cy="13" r="1.2" fill="var(--white)"/>
  </svg>
  <div class="service-label" style="left:331px;top:72px">catering</div>
  <div class="rule" style="left:279px;top:110px;width:112px"></div>

  <svg class="service-icon" style="left:276px;top:124px" width="42" height="42" viewBox="0 0 38 38" aria-hidden="true">
    <circle cx="19" cy="19" r="17" fill="none" stroke="var(--bright-red)" stroke-width="2.5"/>
    <path d="M14 20 a4 4 0 1 1 3 -7 a4 4 0 0 1 5 0 a4 4 0 1 1 3 7 v5 h-11z" fill="none" stroke="var(--white)" stroke-width="1.3"/>
  </svg>
  <div class="service-label" style="left:331px;top:133px">rent-a-chef<br>events</div>
  <div class="rule" style="left:279px;top:176px;width:112px"></div>

  <svg class="service-icon" style="left:276px;top:189px" width="42" height="42" viewBox="0 0 38 38" aria-hidden="true">
    <circle cx="19" cy="19" r="17" fill="none" stroke="var(--bright-red)" stroke-width="2.5"/>
    <ellipse cx="14" cy="18" rx="5" ry="2" fill="none" stroke="var(--white)" stroke-width="1.1"/>
    <path d="M9 18 v5 a5 2 0 0 0 10 0 v-5" fill="none" stroke="var(--white)" stroke-width="1.1"/>
    <ellipse cx="24" cy="15" rx="5" ry="2" fill="none" stroke="var(--white)" stroke-width="1.1"/>
    <path d="M19 15 v5 a5 2 0 0 0 10 0 v-5" fill="none" stroke="var(--white)" stroke-width="1.1"/>
  </svg>
  <div class="service-label" style="left:331px;top:198px">sushi making<br>classes</div>

  <div class="tagline">
    <span class="tagline-line">sushi</span>
    <span class="tagline-line">experience</span>
    <span class="tagline-line">elevated</span>
  </div>

  <div class="rule" style="left:42px;top:272px;width:523px"></div>

  <div class="abs" style="left:44px;top:300px">
    <div class="city">Edmond</div>
    <div class="address">4870 SE 52nd,<br>Edmond, OK 73025</div>
  </div>
  <div class="abs" style="left:167px;top:300px">
    <div class="city">NW-OKC</div>
    <div class="address">2915 E Larkspur Rd,<br>Oklahoma City, OK 73159</div>
  </div>

  <svg class="abs" style="left:321px;top:296px" width="22" height="22" viewBox="0 0 16 16" aria-hidden="true">
    <circle cx="8" cy="8" r="7" fill="none" stroke="var(--bright-red)" stroke-width="1.3"/>
    <path d="M5.5 5 l1.5 -.5 1 2 -1 .8 a4 4 0 0 0 2 2 l.8 -1 2 1 -.5 1.5 c-3 .5 -6.5 -3 -5.8 -5.8z" fill="var(--white)"/>
  </svg>
  <div class="abs" style="left:352px;top:292px;font-size:21px;line-height:28px">(405) 555-0147</div>

  <svg class="abs" style="left:321px;top:334px" width="22" height="22" viewBox="0 0 16 16" aria-hidden="true">
    <circle cx="8" cy="8" r="7" fill="none" stroke="var(--bright-red)" stroke-width="1.3"/>
    <rect x="4.5" y="5.5" width="7" height="5" fill="none" stroke="var(--white)" stroke-width=".9"/>
    <path d="M4.5 5.5 8 8.3 11.5 5.5" fill="none" stroke="var(--white)" stroke-width=".9"/>
  </svg>
  <div class="abs" style="left:352px;top:331px;font-size:18px;line-height:28px">catering@thekelpdockok.com</div>

  <div class="web-band" style="left:291px;top:375px;width:288px;height:28px;font-size:21px">www.thekelpdockok.com</div>

  <div class="door">
    <div class="door-inner">
      <div class="brand" style="left:28px;top:154px">
        <div class="brand-dot" style="width:12px;height:12px"></div>
        <div class="brand-name" style="font-size:36px"><span>the</span><span>kelp</span><span>dock</span></div>
      </div>
    </div>
  </div>
</section>

</body>
</html>
```